New label for vitamin and supplement products

We are a a Vitamin and Supplement company called Bright Harbor. We have been in business for 30 years and the branding needs a significant refresh.

We need all new packaging, including logo, colors, etc.

We want to have a fresh, clean, brand that inspires confidence and quality.

The website is Brightharbor.com and will also be updated.

Please ask any questions. Every idea is a good one.

```html
<!DOCTYPE html>
<html lang="en">
<head>
<meta charset="UTF-8">
<title>Bright Harbor – Daily Core Minerals Label</title>
<link href="https://fonts.googleapis.com/css2?family=Arimo:wght@400;700&display=swap" rel="stylesheet">
<style>
  :root {
    --backdrop: #a3a3a3;
    --label-white: #f7f7f7;
    --ink: #1a1a1a;
    --brand-tab: #1c1c1c;
    --green: #8cc63f;
    --green-light: #a6d94e;
    --white: #ffffff;
  }
  * { margin: 0; padding: 0; box-sizing: border-box; }
  html, body {
    width: 1200px; height: 900px; overflow: hidden;
    background: var(--backdrop);
    font-family: "Arimo", Arial, sans-serif;
  }
  .label {
    position: absolute; left: 250px; top: 20px;
    width: 700px; height: 860px;
    background: var(--label-white);
    overflow: hidden;
  }
  .brand-tab {
    position: absolute; left: 75px; top: 0;
    width: 110px; height: 258px;
    background: var(--brand-tab);
  }
  .brand-name {
    position: absolute; left: 215px; top: 78px;
    font-weight: 700; font-size: 52px; color: var(--ink);
    letter-spacing: 0.5px; white-space: nowrap;
  }
  .strength-strip {
    position: absolute; left: 0; top: 205px;
    width: 46px; height: 490px;
    background: var(--green);
    border-radius: 0 12px 12px 0;
    display: flex; align-items: center; justify-content: center;
  }
  .strength-strip span {
    transform: rotate(-90deg);
    white-space: nowrap;
    color: var(--white); font-size: 19px; letter-spacing: 7px;
  }
  .product-title {
    position: absolute; left: 95px; top: 330px;
    font-weight: 700; font-size: 100px; line-height: 0.88;
    color: var(--ink); letter-spacing: -1px; white-space: nowrap;
  }
  .product-sub {
    position: absolute; left: 97px; top: 522px;
    font-size: 52px; color: var(--ink); white-space: nowrap;
  }
  .product-sub b { font-weight: 700; }
  .bottom-band { position: absolute; left: 0; bottom: 0; width: 700px; height: 150px; }
  .dose {
    position: absolute; left: 180px; top: 770px;
    font-size: 38px; color: var(--ink); white-space: nowrap;
  }
  .dose b { font-weight: 700; }
  .supplement-note {
    position: absolute; left: 164px; top: 828px;
    font-size: 15px; color: var(--white); letter-spacing: 0.3px; white-space: nowrap;
  }
  .count {
    position: absolute; left: 610px; top: 750px;
    color: var(--white); text-align: center; line-height: 1;
  }
  .count .number { font-weight: 700; font-size: 54px; display: block; }
  .count .unit { font-size: 17px; display: block; margin-top: 2px; }
  .caplet-icon { position: absolute; left: 570px; top: 762px; }
</style>
</head>
<body>
  <main class="label">
    <div class="brand-tab"></div>
    <div class="brand-name">Bright Harbor</div>

    <div class="strength-strip"><span>EXTRA STRENGTH</span></div>

    <h1 class="product-title">DAILY CORE<br>MINERALS</h1>
    <p class="product-sub"><b>17</b> Vital Minerals</p>

    <svg class="bottom-band" viewBox="0 710 700 150" width="700" height="150">
      <path d="M380 860 L405 795 C425 765 455 752 505 745 L700 728 L700 860 Z" fill="var(--green)"/>
      <path d="M470 860 L535 748 L572 745 L505 860 Z" fill="var(--green-light)"/>
      <path d="M530 860 L602 740 L630 738 L558 860 Z" fill="var(--green-light)" opacity="0.7"/>
      <rect x="0" y="822" width="700" height="38" fill="var(--green)"/>
      <path d="M455 860 L481 822 L530 822 L504 860 Z" fill="var(--green-light)"/>
      <path d="M515 860 L541 822 L568 822 L542 860 Z" fill="var(--green-light)" opacity="0.7"/>
    </svg>

    <svg class="caplet-icon" width="30" height="72" viewBox="0 0 30 72">
      <rect x="2" y="2" width="26" height="68" rx="13" fill="none" stroke="var(--white)" stroke-width="3"/>
      <line x1="2" y1="36" x2="28" y2="36" stroke="var(--white)" stroke-width="3"/>
      <path d="M11 10 Q18 10 18 18" fill="none" stroke="var(--white)" stroke-width="3" stroke-linecap="round"/>
    </svg>

    <div class="dose"><b>2400</b>mg</div>
    <div class="supplement-note">DIETARY SUPPLEMENT</div>
    <div class="count"><span class="number">60</span><span class="unit">Caplets</span></div>
  </main>
</body>
</html>
```